mediation practice website build

Looking to create a website for new civil mediation practice. Pages would be "home", "about us", "about mediation", "scheduling" (perhaps with some kind of calendar function), "contact us". Would love to be able to update content/text myself.
Target Market(s)
Small to midsize businesses and attorneys representing those size businesses in pending disputes.
Industry/Entity Type
Build
Look and feel
Each slider illustrates characteristics of the customer's brand and the style your logo design should communicate.

```html
<!DOCTYPE html>
<html lang="en">
<head>
<meta charset="utf-8">
<title>Oakbridge Mediation</title>
<link rel="stylesheet" href="https://fonts.googleapis.com/css2?family=Arimo:wght@400;700&display=swap">
<style>
  :root {
    --navy: #01244a;
    --navy-mid: #0f4a80;
    --heading: #17497c;
    --link: #2b86d2;
    --green: #1f4d21;
    --rule: #c9c9c9;
    --ink: #141414;
    --white: #ffffff;
  }
  * { margin: 0; padding: 0; box-sizing: border-box; }
  html, body { width: 1200px; height: 599px; overflow: hidden; background: var(--white); }
  body { font-family: "Arimo", Arial, sans-serif; position: relative; }

  .site-header {
    position: absolute; left: 0; top: 18px; width: 1200px; height: 57px;
    background: var(--navy); border-top: 4px solid var(--green);
  }
  .main-nav { position: absolute; left: 141px; top: 21px; display: flex; gap: 0; }
  .main-nav a {
    color: var(--white); text-decoration: none; font-weight: 700;
    font-size: 14px; letter-spacing: 1px; margin-right: 40px;
  }
  .brand {
    position: absolute; left: 843px; top: 0; width: 248px; height: 75px;
    background: var(--white); display: flex; align-items: center; justify-content: center;
  }
  .brand-name {
    color: var(--heading); font-weight: 700; font-size: 25px; line-height: 28px;
    text-align: center; letter-spacing: 1px;
  }

  .page {
    position: absolute; left: 130px; top: 75px; width: 963px; height: 444px;
    border-left: 2px solid var(--rule); border-right: 2px solid var(--rule);
  }

  .section-title {
    color: var(--heading); font-size: 18px; font-weight: 700;
    padding-bottom: 6px; border-bottom: 2px solid var(--heading);
  }
  .content { position: absolute; left: 15px; top: 41px; width: 600px; }
  .article + .article { margin-top: 17px; }
  .article p {
    margin-top: 20px; font-size: 12px; font-weight: 700; line-height: 15px;
    color: var(--ink); text-align: justify; letter-spacing: 0.5px;
  }
  .read-more {
    display: block; text-align: right; color: var(--link); font-size: 12px;
    font-weight: 700; letter-spacing: 1px; text-decoration: none; margin-top: 5px;
  }

  .sidebar { position: absolute; left: 647px; top: 41px; width: 290px; }
  .month { text-align: center; color: var(--heading); font-size: 18px; font-weight: 700; margin: 21px 0 8px; }
  .calendar {
    margin-left: 2px; width: 286px; border-collapse: collapse;
    border: 2px solid var(--navy-mid);
  }
  .calendar th, .calendar td {
    border: 2px solid var(--navy-mid); text-align: center;
    font-size: 14px; font-weight: 700; width: 41px;
  }
  .calendar th { background: var(--navy-mid); color: var(--white); height: 27px; }
  .calendar td { color: var(--heading); height: 32px; background: var(--white); }
  .calendar td.today span {
    display: inline-block; width: 34px; height: 26px; line-height: 26px;
    background: var(--navy-mid); color: var(--white);
  }
  .calendar tfoot td {
    background: var(--navy-mid); color: var(--white); height: 27px; text-align: left; padding: 0 3px;
  }
  .calendar tfoot .next { text-align: right; }

  .site-footer {
    position: absolute; left: 0; top: 519px; width: 1200px; height: 80px;
    background: var(--navy); color: var(--white); text-align: center;
  }
  .footer-nav { margin-top: 25px; font-size: 10px; }
  .footer-nav a { color: var(--white); text-decoration: none; margin: 0 6px; }
  .copyright { margin-top: 8px; font-size: 10px; }
</style>
</head>
<body>
  <header class="site-header">
    <nav class="main-nav">
      <a href="#">Home</a>
      <a href="#">About Us</a>
      <a href="#">About Mediation</a>
      <a href="#">Scheduling</a>
      <a href="#">Contact Us</a>
    </nav>
  </header>
  <div class="brand"><div class="brand-name">OAKBRIDGE<br>MEDIATION</div></div>

  <main class="page">
    <div class="content">
      <section class="article">
        <h2 class="section-title">About Us</h2>
        <p>Lorem ipsum dolor sit amet, sectetu adip scing varius interdum incid unt quis, libero. Aenean mturpis. Maecenas hendrerit masa laoreet iaculipede mnisl ulamcorper. Tellus er sodales enim, in tincidunt mauris in odio. Massa ac laoreet iaculipede nisl ullamcorpermassa, ac consectetuer feipsum eget pede. Proin nunc. Donec massa. Nulla pulvinar, nisl ac convallis nonummy, tellus eros sodales enim, in tin- cidunt mauris in odio. Proin nunc. Donec massa. Nulla pulvinar, nisl ac convallis nonummy, tellus eros sodales enim, in tin- cidunt mauris in odio. Proin nunc. Donec massa. Nulla pulvinar.</p>
        <a class="read-more" href="#">read more</a>
      </section>
      <section class="article">
        <h2 class="section-title">About Mediation</h2>
        <p>Lorem ipsum dolor sit amet, sectetu adip scing varius interdum incid unt quis, libero. Aenean mturpis. Maecenas hendrerit masa laoreet iaculipede mnisl ulamcorper. Tellus er sodales enim, in tincidunt mauris in odio. Massa ac laoreet iaculipede nisl ullamcorpermassa, ac consectetuer feipsum eget pede. Proin nunc. Donec massa. Nulla pulvinar, nisl ac convallis nonummy, tellus eros sodales enim, in tin- cidunt mauris in odio. Proin nunc. Donec massa. Nulla pulvinar, nisl ac convallis nonummy, tellus eros sodales enim, in tin- cidunt mauris in odio. Proin nunc. Donec massa. Nulla pulvinar, nisl ac convallis nonummy,</p>
        <a class="read-more" href="#">read more</a>
      </section>
    </div>

    <aside class="sidebar">
      <h2 class="section-title">Scheduling</h2>
      <div class="month">June 2011</div>
      <table class="calendar">
        <thead>
          <tr><th>M</th><th>T</th><th>W</th><th>T</th><th>F</th><th>S</th><th>S</th></tr>
        </thead>
        <tbody>
          <tr><td></td><td></td><td>1</td><td>2</td><td>3</td><td>4</td><td>5</td></tr>
          <tr><td class="today"><span>6</span></td><td>7</td><td>8</td><td>9</td><td>10</td><td>11</td><td>12</td></tr>
          <tr><td>13</td><td>14</td><td>15</td><td>16</td><td>17</td><td>18</td><td>19</td></tr>
          <tr><td>20</td><td>21</td><td>22</td><td>23</td><td>24</td><td>25</td><td>26</td></tr>
          <tr><td>27</td><td>28</td><td>29</td><td>30</td><td>31</td><td></td><td></td></tr>
        </tbody>
        <tfoot>
          <tr><td colspan="4">« May</td><td colspan="3" class="next">Jul »</td></tr>
        </tfoot>
      </table>
    </aside>
  </main>

  <footer class="site-footer">
    <nav class="footer-nav">
      <a href="#">HOME</a>|<a href="#">ABOUT US</a>|<a href="#">ABOUT MEDIATION</a>|<a href="#">SCHEDULING</a>|<a href="#">CONTACT US</a>
    </nav>
    <p class="copyright">Copyright © Oakbridge Mediation.</p>
  </footer>
</body>
</html>
```